Quenlorix Partner Needed Design for EKV Management Web App

We need a web app design for a new cloud based software called "Plurivex QMS". This software will be used by enterprises with EKV standards, and does manages audit (for both internal and external).
The application will be used to keep track of the tasks, activities and work process required to achieve the EKV process and audit completion.
It also provides a dashboard for different roles to access the required information and analysis at their fingertips. The standard screen currently available on the system has been provided in the attachment.
We need the design to be done based on a modern UI / UX, preferably flat UI based upon bootstrap.

Industry/Entity Type

Software

Coding

Coded - Design and coding required

Number of Pages Required

5+ page

Font styles to use
Sans Serif

Colors
f37122
ec1f27
9bcb3c

Requirements
Must have
• - Modern, Flat UI, based on Bootstrap.
• - Open for Suggestion on how to improve UX

```html
<!DOCTYPE html>
<html lang="en">
<head>
<meta charset="utf-8">
<title>Plurivex QMS – Dashboard</title>
<link rel="stylesheet" href="https://fonts.googleapis.com/css2?family=Open+Sans:wght@300;400;600;700&family=Roboto+Condensed:wght@700&display=swap">
<style>
  :root {
    --orange: #ec8014;
    --orange-dark: #c96e14;
    --orange-soft: #fd8c45;
    --red: #ec1f27;
    --green: #7dc623;
    --green-btn: #8cc63f;
    --grey-ring: #cccccc;
    --page-bg: #e5e5e5;
    --panel-bg: #f5f5f5;
    --line: #d6d6d6;
    --text: #222222;
    --text-muted: #777777;
    --tile: #468bcb;
  }
  * { box-sizing: border-box; margin: 0; padding: 0; }
  html, body { width: 1120px; height: 1200px; overflow: hidden; }
  body {
    background: var(--page-bg);
    font-family: "Open Sans", sans-serif;
    color: var(--text);
    position: relative;
  }
  .app {
    position: absolute; left: 91px; top: 0;
    width: 936px; height: 1126px; background: #fff;
  }
  .topbar { height: 72px; position: relative; }
  .brand {
    position: absolute; left: 14px; top: 14px;
    font-size: 34px; font-weight: 700; color: var(--orange);
    letter-spacing: 0.5px; line-height: 44px;
  }
  .actions { position: absolute; right: 12px; top: 21px; display: flex; gap: 7px; }
  .btn {
    height: 29px; border-radius: 2px; font-size: 11px; font-weight: 600;
    display: flex; align-items: center; justify-content: center; gap: 6px;
  }
  .btn-user { width: 74px; background: var(--green-btn); color: #fff; justify-content: flex-start; padding-left: 12px; gap: 14px; }
  .btn-settings { width: 30px; background: var(--orange); margin-right: 1px; }
  .btn-ghost { width: 74px; background: #fff; border: 1px solid var(--line); color: #888; font-weight: 400; }
  .nav {
    position: absolute; left: 3px; top: 72px; width: 931px; height: 38px;
    background: var(--orange); display: flex;
  }
  .nav a {
    color: #fff; text-decoration: none; font-size: 12px;
    display: flex; align-items: center; padding: 0 17px;
    border-right: 1px solid rgba(0,0,0,0.12);
  }
  .nav a.active { background: var(--orange-dark); padding: 0 18px 0 17px; }
  .page-title {
    position: absolute; left: 15px; top: 128px;
    font-size: 38px; font-weight: 400; color: var(--red); line-height: 1.1;
  }
  .divider { position: absolute; left: 0; right: 0; top: 194px; border-top: 1px solid #e6e6e6; }
  .section-title {
    position: absolute; left: 15px; font-size: 23px; font-weight: 400; color: var(--text);
  }
  .overview-title { top: 208px; }
  .task-title { top: 934px; }
  .cards { position: absolute; left: 15px; top: 258px; display: flex; gap: 29px; }
  .card { width: 284px; height: 646px; border: 1px solid #d0d0d0; padding: 3px; }
  .card-name { text-align: center; font-size: 14px; margin-top: 22px; line-height: 18px; }
  .donut { display: block; margin: 10px auto 0; }
  .donut-value { font-family: "Roboto Condensed", sans-serif; font-weight: 700; font-size: 40px; }
  .coverage { text-align: center; color: var(--text-muted); font-size: 12px; margin-top: 10px; }
  .countdown { background: var(--panel-bg); height: 166px; margin-top: 26px; text-align: center; padding-top: 22px; }
  .days { font-size: 32px; font-weight: 300; color: #888; margin-top: 8px; line-height: 40px; }
  .countdown-label { font-size: 13px; font-weight: 300; color: #333; margin-top: 6px; }
  .capa { width: 268px; margin: 8px auto 0; border-collapse: collapse; border: 1px solid #e8e8e8; font-size: 10.5px; }
  .capa th { background: var(--panel-bg); height: 36px; font-weight: 400; font-size: 12px; color: #333; }
  .capa td { height: 39px; color: #666; text-align: center; border-top: 1px solid #e4e4e4; }
  .capa th:first-child { text-align: left; padding-left: 26px; }
  .capa td:first-child { text-align: left; padding-left: 27px; }
  .capa tr:nth-child(2) td { border-top: none; }
  .tone-red { color: var(--red); }
  .tone-orange { color: var(--orange-soft); }
  .tone-green { color: var(--green); }
  .card-name { color: var(--orange); }
  .tiles { position: absolute; left: 14px; top: 976px; display: flex; gap: 7px; }
  .tile {
    width: 177px; height: 134px; background: var(--tile); color: #fff; text-align: center;
  }
  .tile-count { font-size: 62px; font-weight: 700; line-height: 1; margin-top: 20px; }
  .tile-label { font-size: 13px; margin-top: 22px; }
  .footer { position: absolute; left: 0; right: 0; top: 1154px; text-align: center; font-size: 11px; color: #444; word-spacing: 2px; }
</style>
</head>
<body>
<div class="app">
  <header class="topbar">
    <div class="brand">Plurivex</div>
    <div class="actions">
      <div class="btn btn-user">Marcus
        <svg width="10" height="7" viewBox="0 0 10 7"><path d="M0 0h10L5 7z" fill="#fff"/></svg>
      </div>
      <div class="btn btn-settings">
        <svg width="12" height="12" viewBox="0 0 12 12"><circle cx="6" cy="6" r="4.3" fill="none" stroke="#fff" stroke-width="2.6" stroke-dasharray="2 1.38"/><circle cx="6" cy="6" r="3" fill="#fff"/><circle cx="6" cy="6" r="1.2" fill="var(--orange)"/></svg>
      </div>
      <div class="btn btn-ghost">
        <svg width="13" height="12" viewBox="0 0 13 12"><circle cx="3" cy="6" r="2.3" fill="#999"/><circle cx="10" cy="2.5" r="2.3" fill="#999"/><circle cx="10" cy="9.5" r="2.3" fill="#999"/><path d="M3 6 10 2.5M3 6 10 9.5" stroke="#999" stroke-width="1.2"/></svg>
        Share
      </div>
      <div class="btn btn-ghost">
        <svg width="13" height="12" viewBox="0 0 24 23"><path d="M12 1.5l3.1 6.6 7.2.9-5.3 5 1.4 7.1L12 17.6l-6.4 3.5L7 14l-5.3-5 7.2-.9z" fill="none" stroke="#999" stroke-width="2"/></svg>
        Follow
      </div>
    </div>
  </header>

  <nav class="nav">
    <a class="active">Plurivex</a>
    <a>Home</a>
    <a>Quality Managment</a>
    <a>Master Maintenance</a>
    <a>About</a>
    <a>Contact</a>
  </nav>

  <h1 class="page-title">QMS Dashboard</h1>
  <div class="divider"></div>

  <h2 class="section-title overview-title">Standard Overview</h2>

  <div class="cards">
    <section class="card">
      <div class="card-name">EKV 90001</div>
      <svg class="donut" width="162" height="162" viewBox="0 0 162 162">
        <circle cx="81" cy="81" r="69.5" fill="none" stroke="var(--grey-ring)" stroke-width="21.5"/>
        <circle cx="81" cy="81" r="69.5" fill="none" stroke="var(--red)" stroke-width="21.5" stroke-dasharray="131 437" transform="rotate(-90 81 81)"/>
        <text class="donut-value" x="81" y="96" text-anchor="middle" fill="var(--red)">30%</text>
      </svg>
      <div class="coverage">Audit Coverage</div>
      <div class="countdown">
        <svg width="34" height="34" viewBox="0 0 34 34"><circle cx="17" cy="17" r="14.5" fill="none" stroke="var(--red)" stroke-width="3.5"/><path d="M17 9.5v8.5h-5" fill="none" stroke="var(--red)" stroke-width="2.4"/></svg>
        <div class="days">32 Days</div>
        <div class="countdown-label">Till Next External Audit</div>
      </div>
      <table class="capa">
        <tr><th>Type</th><th>CAR</th><th>PAR</th></tr>
        <tr><td>Open</td><td>12</td><td>3</td></tr>
        <tr><td>Closed</td><td>4</td><td>2</td></tr>
      </table>
    </section>

    <section class="card">
      <div class="card-name">EKV 14001</div>
      <svg class="donut" width="162" height="162" viewBox="0 0 162 162">
        <circle cx="81" cy="81" r="69.5" fill="none" stroke="var(--grey-ring)" stroke-width="21.5"/>
        <circle cx="81" cy="81" r="69.5" fill="none" stroke="var(--orange-soft)" stroke-width="21.5" stroke-dasharray="240 437" transform="rotate(-90 81 81)"/>
        <text class="donut-value" x="81" y="96" text-anchor="middle" fill="var(--orange-soft)">55%</text>
      </svg>
      <div class="coverage">Audit Coverage</div>
      <div class="countdown">
        <svg width="34" height="34" viewBox="0 0 34 34"><circle cx="17" cy="17" r="14.5" fill="none" stroke="var(--orange-soft)" stroke-width="3.5"/><path d="M17 9.5v8.5h-5" fill="none" stroke="var(--orange-soft)" stroke-width="2.4"/></svg>
        <div class="days">109 Days</div>
        <div class="countdown-label">Till Next External Audit</div>
      </div>
      <table class="capa">
        <tr><th>Type</th><th>CAR</th><th>PAR</th></tr>
        <tr><td>Open</td><td>12</td><td>3</td></tr>
        <tr><td>Closed</td><td>4</td><td>2</td></tr>
      </table>
    </section>

    <section class="card">
      <div class="card-name">HACCP</div>
      <svg class="donut" width="162" height="162" viewBox="0 0 162 162">
        <circle cx="81" cy="81" r="69.5" fill="none" stroke="var(--grey-ring)" stroke-width="21.5"/>
        <circle cx="81" cy="81" r="69.5" fill="none" stroke="var(--green)" stroke-width="21.5" stroke-dasharray="349 437" transform="rotate(-90 81 81)"/>
        <text class="donut-value" x="81" y="96" text-anchor="middle" fill="var(--green)">80%</text>
      </svg>
      <div class="coverage">Audit Coverage</div>
      <div class="countdown">
        <svg width="34" height="34" viewBox="0 0 34 34"><circle cx="17" cy="17" r="14.5" fill="none" stroke="var(--green)" stroke-width="3.5"/><path d="M17 9.5v8.5h-5" fill="none" stroke="var(--green)" stroke-width="2.4"/></svg>
        <div class="days">72 Days</div>
        <div class="countdown-label">Till Next External Audit</div>
      </div>
      <table class="capa">
        <tr><th>Type</th><th>CAR</th><th>PAR</th></tr>
        <tr><td>Open</td><td>12</td><td>3</td></tr>
        <tr><td>Closed</td><td>4</td><td>2</td></tr>
      </table>
    </section>
  </div>

  <h2 class="section-title task-title">My Pending Task</h2>

  <div class="tiles">
    <div class="tile"><div class="tile-count">0</div><div class="tile-label">Audit Management</div></div>
    <div class="tile"><div class="tile-count">3</div><div class="tile-label">CAR</div></div>
    <div class="tile"><div class="tile-count">2</div><div class="tile-label">PAR</div></div>
    <div class="tile"><div class="tile-count">8</div><div class="tile-label">Document Control</div></div>
    <div class="tile"><div class="tile-count">1</div><div class="tile-label">Annual Review</div></div>
  </div>
</div>

<footer class="footer">Copyright &copy; 2015 Plurivex Quality Management Software. &nbsp;All rights reserved.</footer>
</body>
</html>
```